African homeware retailer needs a web page design

We need a web page design for a new homeware and accessories store based in Johannesburg, South Africa. Our store carries modern African inspired items from designers that support social development and poverty alleviation initiatives. We have a particular preference for outfits that are centred on the empowerment of women.

Our business celebrates the skill, design and product of African craft and the work of designers looking to take that forward in a socially beneficial way (creating employment, developing skills, supporting local crafts people etc). We aim to carry items and inspirations from all over the African continent.

We would like to see a design that communicates African beauty and elegance without the typical tribal references that are made in reference to African craft or art.

We would like the web page to be stylish, uncomplicated, modern, captivating and appealing to the discerning customer. A similar value proposition is that of http://www.lindqvartworks.example/.

This is an e-commerce website which must be attractive to both individual buyers and design professionals so the website needs to look professional.

Here are links to some websites we like:
http://www.corvanhomes.example/
http://www.tesmoly.example/

Our logo is attached to the brief.

Target Market(s)

Our target market is female, age 20-50. However should not alienate the design conscious male customer therefore

Industry/Entity Type

E-Commerce

Requirements
Must have
• - A featured product banner which includes a photograph and text. This should be easy to edit as we will be changing the featured product regularly
- An easily expendable products section with categories. Examples of categories could be cushions, bedding, crockery etc. Should be easy to add new categories as well as new product pictures
- Home/landing page should be uncluttered
- Should use the logo and should be easy to change the logo which we have in various colour combinations. We plan to change the logo colours depending on circumstance e.g. make it red and white around Valentines day (similar to the way Zentrix frequently changes the logo on their landing page)

```html
<!DOCTYPE html>
<html lang="en">
<head>
<meta charset="utf-8">
<title>Kaya Nuru – Homeware & Accessories</title>
<link rel="stylesheet" href="https://fonts.googleapis.com/css2?family=Roboto:wght@400;500;700&family=Open+Sans:wght@700;800&display=swap">
<style>
:root{
  --green:#0f7a5a;
  --green-dark:#0b5e45;
  --orange:#f05a35;
  --band:#f08a5f;
  --pink:#e9cec8;
  --text:#333;
  --muted:#666;
  --line:#ddd;
  --page-bg:#ececec;
  --dark-bar:rgba(40,40,40,.82);
}
*{box-sizing:border-box;margin:0;padding:0}
html,body{width:809px;height:1200px;overflow:hidden}
body{background:var(--page-bg);font-family:Roboto,Arial,sans-serif;color:var(--text);position:relative}
.page{position:absolute;left:94px;top:0;width:620px;height:1200px;background:#fff;border-top:2px solid #555}
.abs{position:absolute}
.toplinks{right:12px;top:10px;font-size:8px;color:#777;word-spacing:2px}
.toplinks span{margin:0 5px}
.topline{left:8px;right:8px;top:26px;border-top:1px solid var(--line)}
.brand{left:6px;top:34px;width:80px;text-align:center}
.brand-mark{width:14px;height:14px;background:var(--orange);margin:14px auto 6px}
.brand-name{font-size:13px;font-weight:500;color:var(--orange);letter-spacing:1px;line-height:1.1}
.call{left:322px;top:44px;font-size:8px;color:#444;display:flex;align-items:center;gap:4px}
.call b{font-weight:400;font-size:11px;color:#222}
.call em{font-style:normal;color:var(--green);font-size:9px}
.search{left:228px;top:62px;width:208px;height:26px;border:1px solid #ccc;font-size:8px;color:#999;padding:8px 9px}
.search-btn{left:436px;top:62px;width:27px;height:26px;background:var(--orange)}
.auth{left:502px;top:43px;font-size:7.5px;color:#444;display:flex;gap:16px}
.cart-icon{left:500px;top:62px;width:28px;height:26px;background:var(--green)}
.cart-total{left:528px;top:62px;width:85px;height:26px;background:#555;color:#fff;font-size:7.5px;padding:9px 8px}
.nav{left:7px;top:133px;width:607px;height:28px;background:var(--green);display:flex;font-size:9.5px;color:#fff}
.nav a{display:flex;align-items:center;padding:0 14px;border-right:1px solid rgba(255,255,255,.25);text-decoration:none;color:#fff}
.nav a.active{background:var(--orange);padding:0 15px}
.nav a:last-child{border:none;margin-left:auto;padding-right:19px}
.hero{left:5px;top:170px;width:608px;height:266px;background:var(--pink);border:1px solid #c9a29a}
.hero h1{position:absolute;left:52px;top:30px;font-family:'Open Sans',sans-serif;font-weight:700;font-size:26px;line-height:33px;color:#2b2b2b}
.hero p{position:absolute;left:55px;top:100px;width:210px;font-size:15px;line-height:20px;color:#222}
.read-more{position:absolute;left:49px;top:176px;width:202px;height:34px;background:var(--green);border-radius:3px;color:#fff;font-family:'Open Sans',sans-serif;font-weight:800;font-size:20px;letter-spacing:1px;display:flex;align-items:center;padding-left:17px;gap:14px}
.read-more i{width:22px;height:22px;border-radius:50%;border:2px solid #fff;display:inline-block}
.dots{position:absolute;left:56px;top:242px;display:flex;gap:5px}
.dots i{width:10px;height:10px;border-radius:50%;background:var(--green)}
.dots i:first-child{background:var(--orange)}
.diamond{position:absolute;width:110px;height:110px;clip-path:polygon(50% 0,100% 50%,50% 100%,0 50%)}
.band{left:8px;top:447px;width:606px;height:25px;background:linear-gradient(90deg,#ef8a62,#f29a70 50%,#ef8a62);color:#fff;font-size:11px;font-weight:500;letter-spacing:.5px;text-align:center;line-height:25px}
.tile{position:absolute;width:192px;height:211px}
.tile .photo{position:absolute;inset:0}
.tile .save{position:absolute;right:0;bottom:30px;width:49px;height:26px;background:var(--green);color:#fff;text-align:right;padding:2px 5px;font-size:6px;line-height:7px}
.tile .save b{display:block;font-size:12px;line-height:15px}
.tile .bar{position:absolute;left:0;right:0;bottom:0;height:30px;background:var(--dark-bar);color:#fff;display:flex;align-items:center}
.tile .bar .name{flex:0 0 111px;padding-left:10px;font-size:11px;border-right:1px solid #888;height:100%;display:flex;align-items:center}
.tile .bar .shop{flex:1;text-align:center;font-size:9px}
.divider{left:8px;right:8px;border-top:1px solid var(--line)}
.h4{font-size:9.5px;font-weight:500;color:#222}
.social{left:10px;top:993px;font-size:7px;color:#555;line-height:11px;width:120px}
.vsep{border-left:1px solid var(--line)}
.news-sub{left:176px;top:989px;font-size:8px;color:#444}
.news-input{left:175px;top:1008px;width:170px;height:22px;border:1px solid #ccc;font-size:7px;color:#888;padding:7px 4px}
.news-go{left:345px;top:1008px;width:26px;height:22px;background:var(--orange);color:#fff;font-size:8px;font-weight:700;text-align:center;line-height:22px}
.fb-box{left:435px;top:988px;width:92px;height:46px;border:1px solid #ddd;display:flex;align-items:center;justify-content:center;gap:4px;font-size:9px;color:var(--orange);font-weight:500}
.fb-box i{width:8px;height:8px;background:var(--orange)}
.like{left:532px;top:1002px;font-size:6.5px;color:#444;line-height:12px}
.like span{border:1px solid #aac;padding:0 4px;background:#eef}
.col ul{list-style:none;margin-top:7px;font-size:8.5px;line-height:14px;color:#333}
.col li::before{content:"» ";}
.contact{font-size:8.5px;line-height:13px;color:#333}
.contact div{display:flex;gap:8px;margin-top:5px}
.contact svg{flex:none}
.foot-brand{left:533px;top:1058px;width:80px;text-align:center}
.copy{left:12px;top:1175px;font-size:8.5px;color:#333}
.cards{right:8px;top:1171px;display:flex;gap:3px}
.cards span{width:30px;height:18px;border:1px solid #bbb;border-radius:2px;font-size:6px;color:#333;display:flex;align-items:center;justify-content:center}
</style>
</head>
<body>
<div class="page">
  <div class="abs toplinks">MY ACCOUNT<span>|</span>MY CART<span>|</span>MY WHISH LIST<span>|</span>CONTACT US</div>
  <div class="abs topline"></div>

  <div class="abs brand"><div class="brand-mark"></div><div class="brand-name">KAYA<br>NURU</div></div>

  <div class="abs call">
    <svg width="10" height="10" viewBox="0 0 10 10"><circle cx="5" cy="5" r="4.4" fill="none" stroke="#444" stroke-width=".8"/><path d="M3.3 2.6l1 1-.5.7a4 4 0 0 0 1.9 1.9l.7-.5 1 1-.8.8C4.8 7.2 2.8 5.2 2.5 3.4z" fill="#444"/></svg>
    Call Us: <b>123 456 7890</b> <em>(24x7)</em>
  </div>
  <div class="abs search">Search...</div>
  <div class="abs search-btn"><svg width="27" height="26" viewBox="0 0 27 26"><circle cx="12.5" cy="11.5" r="4.5" fill="none" stroke="#fff" stroke-width="2"/><path d="M15.5 14.5l4 4" stroke="#fff" stroke-width="2.4"/></svg></div>
  <div class="abs auth"><span>🔒︎ LOGIN</span><span>✎ SIGN UP</span></div>
  <div class="abs cart-icon"><svg width="28" height="26" viewBox="0 0 28 26"><path d="M8 9h2l1.6 6h6.4l1.4-4.5H11" fill="none" stroke="#fff" stroke-width="1.1"/><circle cx="12.5" cy="17" r="1" fill="#fff"/><circle cx="17" cy="17" r="1" fill="#fff"/></svg></div>
  <div class="abs cart-total">0 items(s) - $0.00 ▾</div>

  <nav class="abs nav">
    <a class="active">SHOP NOW</a><a>CUSHIONS</a><a>BEDDING</a><a>CROCKERY</a><a>SALE</a><a>DESIGNER &amp; ARCHITECTS</a><a>PRESS &amp; MENTIONS</a>
  </nav>

  <section class="abs hero">
    <h1>Lorem ipsum<br>dolor sit</h1>
    <p>Lorem ipsum dolor sit amet consectetuer adipiscin lo lorem.</p>
    <div class="read-more">READ MORE <i></i></div>
    <div class="dots"><i></i><i></i><i></i><i></i><i></i></div>
    <div class="diamond" role="img" aria-label="Porcelain tea set" style="left:396px;top:4px;background:linear-gradient(135deg,#2a2a2a,#e8e2d8 55%,#333)"></div>
    <div class="diamond" role="img" aria-label="Woven baskets" style="left:326px;top:76px;background:linear-gradient(135deg,#c9a46a,#3a2a1a 60%,#d9b57e)"></div>
    <div class="diamond" role="img" aria-label="Colourful woven basket" style="left:467px;top:76px;background:linear-gradient(135deg,#f2ece4,#3a5a7a 50%,#c9a04a)"></div>
    <div class="diamond" role="img" aria-label="Tall woven basket" style="left:396px;top:148px;background:linear-gradient(160deg,#eae4dc,#6b4a25 55%,#3b2814)"></div>
  </section>

  <div class="abs band">TOP CATEGORIES</div>

  <div class="tile" style="left:7px;top:484px"><div class="photo" role="img" aria-label="Pile of colourful cushions" style="background:linear-gradient(160deg,#bfc9a0,#8a4a6a 50%,#c0336a)"></div><div class="save">SAVE UP TO<b>40%</b></div><div class="bar"><span class="name">CUSHIONS</span><span class="shop">SHOP NOW ›</span></div></div>
  <div class="tile" style="left:214px;top:484px"><div class="photo" role="img" aria-label="Bed with coral patterned linen" style="background:linear-gradient(160deg,#ece6de,#e5b3a4 50%,#e2584a)"></div><div class="save">SAVE UP TO<b>10%</b></div><div class="bar"><span class="name">BEDDING</span><span class="shop">SHOP NOW ›</span></div></div>
  <div class="tile" style="left:422px;top:484px"><div class="photo" role="img" aria-label="Patterned crockery and teapot" style="background:linear-gradient(160deg,#a99a82,#e6e1d7 50%,#8a7b5e)"></div><div class="save">SAVE UP TO<b>30%</b></div><div class="bar"><span class="name">CROCKERY</span><span class="shop">SHOP NOW ›</span></div></div>
  <div class="tile" style="left:7px;top:709px"><div class="photo" role="img" aria-label="Yellow chair with printed cushion" style="background:linear-gradient(180deg,#f3f3f1,#e9e4d6 55%,#8a6a4a)"></div><div class="save">SAVE UP TO<b>20%</b></div><div class="bar"><span class="name">CHAIRS</span><span class="shop">SHOP NOW ›</span></div></div>
  <div class="tile" style="left:214px;top:709px"><div class="photo" role="img" aria-label="Colourful bangles and polka dot fabric" style="background:linear-gradient(160deg,#3a6a8a,#c23a6a 45%,#2a2a4a)"></div><div class="save">SAVE UP TO<b>5%</b></div><div class="bar"><span class="name">HIPPIE</span><span class="shop">SHOP NOW ›</span></div></div>
  <div class="tile" style="left:422px;top:709px"><div class="photo" role="img" aria-label="Carved wooden candle holders" style="background:linear-gradient(90deg,#e8e6e4,#6a2a1a 30%,#e8e6e4 50%,#6a2a1a 75%,#e8e6e4)"></div><div class="save">SAVE UP TO<b>15%</b></div><div class="bar"><span class="name">AFRICAN CANDLE</span><span class="shop">SHOP NOW ›</span></div></div>

  <div class="abs divider" style="top:954px"></div>
  <div class="abs h4" style="left:10px;top:972px">FOLLOW US</div>
  <div class="abs social">Folkbook · Chirper · Circlo · StreamTube · Tweetly</div>
  <div class="abs vsep" style="left:149px;top:972px;height:56px"></div>
  <div class="abs h4" style="left:175px;top:972px">SIGN UP FOR NEWSLETTER</div>
  <div class="abs news-sub">Signup Here Free Updates &amp; Latest OFFERS!</div>
  <div class="abs news-input">enter your email...</div>
  <div class="abs news-go">GO</div>
  <div class="abs vsep" style="left:402px;top:972px;height:56px"></div>
  <div class="abs h4" style="left:435px;top:972px">FIND US ON FOLKBOOK</div>
  <div class="abs fb-box"><i></i>KAYA NURU</div>
  <div class="abs like"><span>Like</span><br>899 people like this.</div>

  <div class="abs divider" style="top:1045px"></div>
  <div class="abs col" style="left:8px;top:1059px"><div class="h4">INFORMATIONS</div><ul><li>Our Blog</li><li>About Our Shop</li><li>Secure Shopping</li><li>Privacy Policy</li><li>Delivery Informations</li></ul></div>
  <div class="abs vsep" style="left:118px;top:1060px;height:90px"></div>
  <div class="abs col" style="left:134px;top:1059px"><div class="h4">CUSTOMER CARE</div><ul><li>Contact Us</li><li>Site Map</li><li>Top Sales &amp; Bestsellers</li><li>Gift Vouchers</li><li>Best Sellers</li></ul></div>
  <div class="abs vsep" style="left:252px;top:1060px;height:90px"></div>
  <div class="abs col" style="left:268px;top:1059px"><div class="h4">YOUR ACCOUNT</div><ul><li>Order Status</li><li>My Wishlist</li><li>Delivery Address</li><li>Order History</li><li>Newsletter</li></ul></div>
  <div class="abs vsep" style="left:376px;top:1060px;height:90px"></div>
  <div class="abs contact" style="left:394px;top:1059px"><div class="h4">CONTACT US</div>
    <div><svg width="9" height="11" viewBox="0 0 9 11"><path d="M4.5 0a4 4 0 0 1 4 4c0 3-4 7-4 7S.5 7 .5 4a4 4 0 0 1 4-4z" fill="#888"/><circle cx="4.5" cy="4" r="1.5" fill="#fff"/></svg><span>123 Lorem ipsum dolor sit<br>amet ectetue euiolutpat.</span></div>
    <div style="margin-top:9px"><svg width="10" height="10" viewBox="0 0 10 10"><circle cx="5" cy="5" r="4.4" fill="none" stroke="#888" stroke-width=".8"/><path d="M3.3 2.6l1 1-.5.7a4 4 0 0 0 1.9 1.9l.7-.5 1 1-.8.8C4.8 7.2 2.8 5.2 2.5 3.4z" fill="#888"/></svg><span>123 456 7890</span></div>
    <div style="margin-top:7px"><svg width="10" height="8" viewBox="0 0 10 8"><rect x=".5" y=".5" width="9" height="7" fill="none" stroke="#888"/><path d="M.5 .5l4.5 4 4.5-4" fill="none" stroke="#888"/></svg><span>info@kayanuru.example</span></div>
  </div>
  <div class="abs foot-brand"><div class="brand-mark" style="margin-top:8px"></div><div class="brand-name">KAYA<br>NURU</div></div>

  <div class="abs divider" style="top:1166px"></div>
  <div class="abs copy">Copyright © 2014 Kaya Nuru. All rights reserved.</div>
  <div class="abs cards"><span>Cardora</span><span>PayWell</span><span>Vexa</span><span>Roamly</span><span>Meridia</span></div>
</div>
</body>
</html>
```